Bright Oak LLC Brochure

I am attaching a copy of my current brochure. To me it is plain and childish. I would like a brochure with color and pop! I will also attach some pictures from my courses feel free to crop and use. The language on the current brochure should stay somewhat the same in content. If you have better wording feel free to adjust it. I would just like the core content. My logo will also be attached.
Updates

Please incorporate "Health and Safety Educators" in the with the company name. Thank you much!

Font styles to use
Serif
Sans Serif

Colors

Designer to choose colors to be used in the design.

Requirements
Must have
• color and pop, must have my name Bright Oak LLC, tag line "we make learning fun" content to draw parties to the brochure

```html
<!DOCTYPE html>
<html lang="en">
<head>
<meta charset="utf-8">
<title>Bright Oak LLC – Health and Safety Education Flyer</title>
<link href="https://fonts.googleapis.com/css2?family=Raleway:ital,wght@0,300;0,400;0,600;0,700;0,800;1,700&display=swap" rel="stylesheet">
<style>
  :root {
    --backdrop: #e6e6e8;
    --paper: #ffffff;
    --cyan: #2bb3d9;
    --cyan-deep: #1a9cc4;
    --ink: #2e2e33;
    --ink-soft: #6b6b72;
    --ink-light: #9a9aa1;
    --panel-grey: #ececee;
    --dark-box: #2b2b2f;
    --strip-grey: #7c7c84;
    --sunset-top: #f29a4a;
    --sunset-mid: #d9663a;
    --sunset-low: #4a4a52;
  }
  * { margin: 0; padding: 0; box-sizing: border-box; }
  html, body { width: 1200px; height: 858px; overflow: hidden; }
  body {
    background: var(--backdrop);
    font-family: "Raleway", "Helvetica Neue", Arial, sans-serif;
    color: var(--ink);
    position: relative;
  }
  .flyer {
    position: absolute;
    left: 305px; top: 12px;
    width: 590px; height: 834px;
    background: var(--paper);
    overflow: hidden;
    box-shadow: 0 2px 10px rgba(0,0,0,0.08);
  }
  .hero-art { position: absolute; left: 0; top: 0; width: 590px; height: 345px; }
  .hero-tag {
    position: absolute; left: 26px; top: 24px;
    font-size: 10px; font-weight: 700; font-style: italic; color: #fff;
  }
  .hero-title {
    position: absolute; left: 30px; top: 228px; width: 300px;
    font-size: 24px; font-weight: 800; line-height: 1.15; color: #fff;
  }
  .community {
    position: absolute; left: 30px; top: 362px; width: 260px;
  }
  .community-title {
    font-size: 19px; font-weight: 700; color: var(--cyan); line-height: 1.2;
    margin-bottom: 18px;
  }
  .community-text {
    font-size: 15px; font-weight: 300; color: var(--ink-light); line-height: 1.45;
  }
  .course-photos { position: absolute; left: 30px; top: 590px; width: 260px; height: 110px; }
  .classes {
    position: absolute; left: 318px; top: 272px; width: 245px;
    font-size: 7.5px; line-height: 1.6; color: var(--ink-soft);
  }
  .section-label {
    font-size: 8px; font-weight: 700; letter-spacing: 0.4px; color: var(--ink);
    text-transform: uppercase; margin-bottom: 4px;
  }
  .classes p { margin-bottom: 10px; }
  .class-list-label { margin-top: 20px; margin-bottom: 8px; }
  .class-list {
    list-style: none; display: grid; grid-template-columns: 1fr 1fr; gap: 6px 10px;
    font-size: 8px; color: var(--ink);
  }
  .class-list li { display: flex; align-items: flex-start; gap: 5px; line-height: 1.3; }
  .class-list svg { flex: none; width: 10px; height: 10px; margin-top: 0; }
  .instructors {
    position: absolute; left: 290px; top: 560px; width: 300px; height: 230px;
    background: var(--panel-grey); padding: 28px 28px 0 30px;
  }
  .instructors-title {
    font-size: 19px; font-weight: 700; line-height: 1.2; color: var(--ink);
    padding-bottom: 12px; border-bottom: 1px solid #b9b9be; margin-bottom: 14px;
  }
  .instructors p { font-size: 7.5px; line-height: 1.6; color: var(--ink-soft); }
  .contact {
    position: absolute; left: 0; top: 712px; width: 290px; height: 78px;
    background: var(--dark-box); color: #fff; padding: 14px 26px;
  }
  .contact-phone { font-size: 24px; font-weight: 700; letter-spacing: 0.5px; }
  .contact-web { font-size: 10px; font-weight: 600; letter-spacing: 1.5px; color: #bdbdc3; margin-top: 4px; }
  .footer-strip {
    position: absolute; left: 0; top: 790px; width: 590px; height: 44px;
    background: linear-gradient(90deg, #9a9aa1, var(--strip-grey));
    display: flex; align-items: center; justify-content: flex-end; padding-right: 26px;
    font-size: 10px; font-weight: 700; font-style: italic; color: #fff;
  }
</style>
</head>
<body>
  <article class="flyer">
    <svg class="hero-art" viewBox="0 0 590 345" aria-hidden="false">
      <defs>
        <linearGradient id="sunset" x1="0" y1="0" x2="0.4" y2="1">
          <stop offset="0" stop-color="var(--sunset-top)"/>
          <stop offset="0.55" stop-color="var(--sunset-mid)"/>
          <stop offset="1" stop-color="var(--sunset-low)"/>
        </linearGradient>
      </defs>
      <polygon role="img" aria-label="Photo of an instructor performing CPR chest compressions on a man lying outdoors at sunset"
               points="0,0 590,0 590,250 0,330" fill="url(#sunset)"/>
      <polygon points="0,330 590,250 590,258 0,338" fill="var(--cyan)"/>
      <polygon points="334,292 352,290 344,302" fill="var(--cyan)"/>
    </svg>
    <div class="hero-tag">Bright Oak LLC: Health and Safety Education</div>
    <h1 class="hero-title">Providing Health And Safety Needs For All Environments</h1>

    <section class="community">
      <h2 class="community-title">Servicing your community needs to our full capabilities</h2>
      <p class="community-text">At Bright Oak, we give clear, informative, and concise instruction with a variety of hands on training. We take pride in building confidence in our students while making learning fun!</p>
    </section>

    <svg class="course-photos" viewBox="0 0 260 110">
      <defs>
        <linearGradient id="classPhoto" x1="0" y1="0" x2="1" y2="1">
          <stop offset="0" stop-color="#a9b6c4"/>
          <stop offset="1" stop-color="#6e7a88"/>
        </linearGradient>
      </defs>
      <circle cx="45" cy="70" r="38" fill="url(#classPhoto)" stroke="var(--cyan)" stroke-width="3" role="img" aria-label="Course photo of a student during class"/>
      <circle cx="150" cy="42" r="38" fill="url(#classPhoto)" stroke="var(--cyan)" stroke-width="3" role="img" aria-label="Course photo of a group of students"/>
      <circle cx="232" cy="98" r="26" fill="url(#classPhoto)" stroke="var(--cyan)" stroke-width="3" role="img" aria-label="Course photo of a training room"/>
    </svg>

    <section class="classes">
      <h3 class="section-label">Our Classes</h3>
      <p>At Bright Oak we have a broad range of Health and Safety classes to suit your every need. We take pride in our instructors who have years of experience instructing quality built classes. Some courses are pre-written for us by the State of Michigan and insurance companies.</p>
      <p>Though knowledgeable programs we do not let the programs stop there. We compile an ample amount of further research and personal experience to each program to help expand, educate and make your learning experience interactive and fun. There's no dry class in our program, that's a guarantee!</p>
      <h3 class="section-label class-list-label">Some of our classes include</h3>
      <ul class="class-list">
        <li><svg viewBox="0 0 10 10"><circle cx="5" cy="5" r="5" fill="var(--cyan)"/><path d="M2.6 5.2 4.3 6.8 7.4 3.4" stroke="#fff" stroke-width="1.3" fill="none"/></svg>CPR &amp; AED Training</li>
        <li><svg viewBox="0 0 10 10"><circle cx="5" cy="5" r="5" fill="var(--cyan)"/><path d="M2.6 5.2 4.3 6.8 7.4 3.4" stroke="#fff" stroke-width="1.3" fill="none"/></svg>Emergency Vehicle Driving</li>
        <li><svg viewBox="0 0 10 10"><circle cx="5" cy="5" r="5" fill="var(--cyan)"/><path d="M2.6 5.2 4.3 6.8 7.4 3.4" stroke="#fff" stroke-width="1.3" fill="none"/></svg>First Aid Training</li>
        <li><svg viewBox="0 0 10 10"><circle cx="5" cy="5" r="5" fill="var(--cyan)"/><path d="M2.6 5.2 4.3 6.8 7.4 3.4" stroke="#fff" stroke-width="1.3" fill="none"/></svg>Communicable Diseases Training</li>
        <li><svg viewBox="0 0 10 10"><circle cx="5" cy="5" r="5" fill="var(--cyan)"/><path d="M2.6 5.2 4.3 6.8 7.4 3.4" stroke="#fff" stroke-width="1.3" fill="none"/></svg>Respirator Fit Testing</li>
      </ul>
    </section>

    <section class="instructors">
      <h2 class="instructors-title">Your Leading CPR Instructors in Michigan</h2>
      <h3 class="section-label">Our Instructors</h3>
      <p>We have a variety of instructors who have very strong backgrounds in their subject areas making instruction clear and concise. Leaving our students with a full understanding of the topic at hand. Our instructors have backgrounds in EMS, Fire Fighting, Law Enforcement, and Hospital Care. We provide education to the entire state of Michigan.</p>
    </section>

    <div class="contact">
      <div class="contact-phone">(555) 010-4207</div>
      <div class="contact-web">BRIGHTOAKTRAINING.ORG</div>
    </div>

    <footer class="footer-strip">Bright Oak LLC: Health and Safety Education</footer>
  </article>
</body>
</html>
```